Dozing Heron

Need a business card for our restaurant. Restaurant and Bar in the mountains of North Idaho. Rustic looking card

Contact Information for Business Card

rustic design, wood and metal looking, primarily neutral colors

Requirements
Must have
• Name, address, phone number, website, email address

```html
<!DOCTYPE html>
<html lang="en">
<head>
<meta charset="utf-8">
<title>Dozing Heron – Business Card</title>
<link href="https://fonts.googleapis.com/css2?family=Montserrat:wght@400;500;700;800&display=swap" rel="stylesheet">
<style>
  :root {
    --stage: #2b2b2b;
    --card-dark: #111111;
    --card-dark-soft: #2a2a2a;
    --card-light: #ffffff;
    --ink: #111111;
    --ink-soft: #333333;
    --rule: #1a1a1a;
  }
  html, body {
    margin: 0;
    padding: 0;
    width: 1200px;
    height: 875px;
    overflow: hidden;
    background: var(--stage);
    font-family: "Montserrat", sans-serif;
  }
  .stage {
    position: relative;
    width: 1200px;
    height: 875px;
  }
  .card {
    position: absolute;
    top: 289px;
    width: 520px;
    height: 297px;
    border-radius: 18px;
    overflow: hidden;
    box-sizing: border-box;
  }
  /* Back side */
  .card-back {
    left: 50px;
    background: var(--card-dark);
  }
  .card-back .pattern-area {
    position: absolute;
    inset: 0;
    background: linear-gradient(115deg, var(--card-dark-soft) 0%, var(--card-dark) 45%, #0c0c0c 100%);
  }
  .card-back .brand-name {
    position: absolute;
    left: 0;
    right: 0;
    top: 50%;
    transform: translateY(-50%);
    text-align: center;
    color: var(--card-light);
    font-weight: 700;
    font-size: 15px;
    letter-spacing: 0.18em;
    text-transform: uppercase;
  }
  /* Front side */
  .card-front {
    left: 630px;
    background: var(--card-light);
    color: var(--ink);
  }
  .brand-lockup {
    position: absolute;
    top: 26px;
    right: 26px;
    display: flex;
    align-items: center;
    gap: 8px;
  }
  .brand-lockup .brand-dot {
    width: 12px;
    height: 12px;
    border-radius: 50%;
    background: var(--ink);
  }
  .brand-lockup .brand-text {
    font-weight: 700;
    font-size: 14px;
    letter-spacing: 0.14em;
    text-transform: uppercase;
    color: var(--ink);
  }
  .divider-top {
    position: absolute;
    top: 80px;
    left: 26px;
    right: 26px;
    height: 1.5px;
    background: var(--rule);
  }
  .address {
    position: absolute;
    top: 98px;
    right: 26px;
    text-align: right;
    font-size: 11px;
    line-height: 1.4;
    color: var(--ink-soft);
  }
  .person {
    position: absolute;
    left: 26px;
    top: 168px;
  }
  .person .name {
    font-weight: 800;
    font-size: 19px;
    margin: 0;
    line-height: 1.1;
  }
  .person .role {
    font-size: 11px;
    margin: 2px 0 0;
    color: var(--ink-soft);
  }
  .divider-person {
    position: absolute;
    left: 26px;
    top: 212px;
    width: 190px;
    height: 1.5px;
    background: var(--rule);
  }
  .contact-list {
    position: absolute;
    left: 26px;
    top: 222px;
    margin: 0;
    padding: 0;
    list-style: none;
    font-size: 11px;
    line-height: 1;
    color: var(--ink-soft);
  }
  .contact-list li {
    display: flex;
    align-items: center;
    gap: 8px;
    height: 18px;
  }
  .contact-list svg {
    width: 11px;
    height: 11px;
    fill: var(--ink);
  }
</style>
</head>
<body>
<main class="stage">
  <section class="card card-back" aria-label="Card back">
    <div class="pattern-area" role="img" aria-label="Repeating brand motif pattern in glossy black and grey"></div>
    <div class="brand-name">Dozing Heron</div>
  </section>

  <section class="card card-front" aria-label="Card front">
    <div class="brand-lockup">
      <span class="brand-dot"></span>
      <span class="brand-text">Dozing Heron</span>
    </div>
    <div class="divider-top"></div>
    <address class="address" style="font-style:normal">48 Cedar Ridge Road,<br>Pinecrest, USA</address>

    <div class="person">
      <p class="name">Evan Hollis</p>
      <p class="role">Managing Director</p>
    </div>
    <div class="divider-person"></div>

    <ul class="contact-list">
      <li>
        <svg viewBox="0 0 24 24" aria-hidden="true"><path d="M6.6 10.8a15 15 0 0 0 6.6 6.6l2.2-2.2a1 1 0 0 1 1-.25 11.4 11.4 0 0 0 3.6.6 1 1 0 0 1 1 1V20a1 1 0 0 1-1 1A17 17 0 0 1 3 4a1 1 0 0 1 1-1h3.5a1 1 0 0 1 1 1c0 1.25.2 2.45.57 3.57a1 1 0 0 1-.25 1z"/></svg>
        <span>(208) 555 0147</span>
      </li>
      <li>
        <svg viewBox="0 0 24 24" aria-hidden="true"><path d="M2 5h20v14H2z M2 5l10 8 10-8" /></svg>
        <span>hello@dozingheron.com</span>
      </li>
      <li>
        <svg viewBox="0 0 24 24" aria-hidden="true"><circle cx="12" cy="12" r="10"/></svg>
        <span>www.dozingheron.com</span>
      </li>
    </ul>
  </section>
</main>
</body>
</html>
```